VORN - Business cards

Business card to be created for Commercial sales staff

Target Market(s)

Commercial businesses

Industry/Entity Type

Commercial

Contact Information for Business Card

Look professional. For commercial clients

Colors
ffffff

Requirements
Must have
• - Vorn Logo
• - Commercial sales staff as postion
• - room for commerical sales manager role
• - person name and their mobile number
• - Website : vornelectrical.com.au
Nice to have
• White background.
• On back of business card just have the logo no other information
Should not have
• Should only have white background on front of card.

```html
<!DOCTYPE html>
<html lang="en">
<head>
<meta charset="utf-8">
<title>Vorn – Business Card</title>
<link rel="stylesheet" href="https://fonts.googleapis.com/css2?family=Roboto:wght@300;400;700&display=swap">
<style>
  :root {
    --page: #ececec;
    --card-white: #f7f6f4;
    --red-deep: #7f0c14;
    --red: #a8161f;
    --red-light: #c22a30;
    --ink: #1e1e20;
    --on-red: #ffffff;
    --on-red-soft: #f1dcdc;
  }
  * { margin: 0; padding: 0; box-sizing: border-box; }
  html, body {
    width: 1200px;
    height: 969px;
    overflow: hidden;
    background: var(--page);
    font-family: "Roboto", Arial, sans-serif;
  }
  .card {
    position: absolute;
    left: 100px;
    top: 200px;
    width: 1000px;
    height: 570px;
    background: var(--card-white);
    overflow: hidden;
    box-shadow: 0 10px 30px rgba(0,0,0,0.15);
  }
  .card__band {
    position: absolute;
    inset: 0;
    width: 1000px;
    height: 570px;
  }
  .brand {
    position: absolute;
    left: 72px;
    top: 118px;
    display: flex;
    align-items: center;
    gap: 20px;
  }
  .brand__dot {
    width: 58px;
    height: 58px;
    border-radius: 50%;
    background: var(--red);
  }
  .brand__name {
    font-weight: 700;
    font-size: 86px;
    letter-spacing: 2px;
    color: var(--ink);
    line-height: 1;
  }
  .person {
    position: absolute;
    right: 42px;
    top: 282px;
    text-align: right;
    color: var(--on-red);
  }
  .person__name {
    font-weight: 400;
    font-size: 32px;
    line-height: 1.2;
  }
  .person__role {
    font-weight: 300;
    font-size: 27px;
    color: var(--on-red-soft);
    margin-top: 4px;
  }
  .contact {
    position: absolute;
    right: 42px;
    top: 382px;
    list-style: none;
    color: var(--on-red-soft);
    font-weight: 300;
    font-size: 24px;
  }
  .contact__item {
    display: flex;
    justify-content: flex-end;
    align-items: center;
    gap: 12px;
    height: 39px;
  }
  .contact__icon {
    width: 24px;
    height: 24px;
    fill: var(--on-red);
  }
</style>
</head>
<body>
  <section class="card" aria-label="Vorn business card, front">
    <svg class="card__band" viewBox="0 0 1000 570" aria-hidden="true">
      <defs>
        <linearGradient id="bandRed" x1="0" y1="0" x2="1" y2="1">
          <stop offset="0" stop-color="var(--red-light)"/>
          <stop offset="0.5" stop-color="var(--red)"/>
          <stop offset="1" stop-color="var(--red-deep)"/>
        </linearGradient>
      </defs>
      <path d="M640 0 C 660 240, 480 470, 270 570 L1000 570 L1000 0 Z" fill="url(#bandRed)"/>
      <path d="M675 70 C 660 290, 520 450, 300 570 C 540 460, 690 300, 675 70 Z" fill="#ffffff" opacity="0.75"/>
    </svg>

    <div class="brand">
      <span class="brand__dot"></span>
      <span class="brand__name">VORN</span>
    </div>

    <div class="person">
      <p class="person__name">Liam Carter</p>
      <p class="person__role">Manager, Commerical Sales</p>
    </div>

    <ul class="contact">
      <li class="contact__item">555 0142 7731
        <svg class="contact__icon" viewBox="0 0 24 24"><path d="M4 8c0-2 3-4 8-4s8 2 8 4v2h-4V8c-1-.6-2.4-1-4-1s-3 .4-4 1v2H4z"/><path d="M7 12h10l3 7H4z"/></svg>
      </li>
      <li class="contact__item">555 0198 4620
        <svg class="contact__icon" viewBox="0 0 24 24"><path d="M7 2h10a1 1 0 0 1 1 1v18a1 1 0 0 1-1 1H7a1 1 0 0 1-1-1V3a1 1 0 0 1 1-1zm1 3v13h8V5zm4 14.2a1 1 0 1 0 0 2 1 1 0 0 0 0-2z"/></svg>
      </li>
      <li class="contact__item">liam@vornelectrical.com.au
        <svg class="contact__icon" viewBox="0 0 24 24"><path d="M3 6h18v12H3z" opacity="0.9"/><path d="M3 6l9 7 9-7" fill="none" stroke="#a8161f" stroke-width="1.6"/></svg>
      </li>
      <li class="contact__item">vornelectrical.com.au
        <svg class="contact__icon" viewBox="0 0 24 24"><circle cx="12" cy="12" r="9"/><path d="M8 7c2 1 3 2 2 4s-3 1-3 3 2 2 2 4M15 6c-1 2 1 3 2 4s-1 3 0 5" fill="none" stroke="#a8161f" stroke-width="1.6"/></svg>
      </li>
    </ul>
  </section>
</body>
</html>
```